Business card design for Plumbing and Gas fitting company

We need a business card design for our plumbing and gas fitting company using the company logo and director details. Design should be modern and eye-catching however kept reasonably simple. This design should be targeted at commercial businesses/work so professionalism is key.

Target Market(s)

Commercial/business

Industry/Entity Type

Plumbing

Contact Information for Business Card

Warren Dohey
Director
027 581 9043
warren@vantorplumbingandgas.example
PO Box 7816
Palmerston North 4472

Font styles to use
Sans Serif

Requirements
Must have
• Logo
• Modern
• Kept simple
Nice to have
• Colour scheme based around logo

```html
<!DOCTYPE html>
<html lang="en">
<head>
<meta charset="utf-8">
<title>Vantor Plumbing &amp; Gas — Business Card</title>
<link href="https://fonts.googleapis.com/css2?family=Poppins:wght@400;500;600&display=swap" rel="stylesheet">
<style>
  :root {
    --navy: #0c3558;
    --card: #ffffff;
    --brand-blue: #1a7cc4;
    --brand-orange: #ec8a36;
    --ink-grey: #6f6f6f;
    --wash-blue: #e3e7f4;
    --wash-peach: #fbe9dc;
  }
  * { box-sizing: border-box; margin: 0; padding: 0; }
  html, body { width: 1200px; height: 900px; overflow: hidden; }
  body {
    background: radial-gradient(ellipse at center, #0f3d65 0%, var(--navy) 70%);
    font-family: "Poppins", sans-serif;
    position: relative;
  }
  .card {
    position: absolute;
    width: 560px;
    height: 320px;
    background: var(--card);
    border-radius: 26px;
    overflow: hidden;
    box-shadow: 0 18px 40px rgba(0, 0, 0, 0.35);
  }
  .card--front { left: 80px; top: 110px; }
  .card--back { left: 560px; top: 470px; }

  .wave-wash {
    position: absolute;
    right: 0;
    top: 0;
    width: 240px;
    height: 320px;
  }

  .brand-name {
    color: var(--brand-blue);
    font-weight: 600;
    letter-spacing: 0.2px;
    white-space: nowrap;
  }
  .card--front .brand-name {
    position: absolute;
    left: 60px;
    top: 128px;
    font-size: 30px;
    display: flex;
    align-items: center;
    gap: 12px;
  }
  .brand-dot {
    width: 18px;
    height: 18px;
    border-radius: 50%;
    background: var(--brand-orange);
    flex: none;
  }
  .front-web {
    position: absolute;
    left: 0;
    right: 0;
    bottom: 26px;
    text-align: center;
    font-size: 11px;
    letter-spacing: 2.5px;
    color: var(--brand-blue);
  }

  .card--back .brand-name {
    position: absolute;
    left: 34px;
    top: 36px;
    font-size: 18px;
    display: flex;
    align-items: center;
    gap: 8px;
  }
  .card--back .brand-dot { width: 12px; height: 12px; }

  .person {
    position: absolute;
    left: 34px;
    top: 104px;
  }
  .person-name {
    font-size: 22px;
    font-weight: 500;
    color: var(--brand-blue);
    letter-spacing: 1px;
    line-height: 1.1;
  }
  .person-role {
    font-size: 12px;
    color: var(--ink-grey);
    letter-spacing: 1.2px;
  }
  .contact-list {
    position: absolute;
    left: 34px;
    top: 170px;
    list-style: none;
  }
  .contact-list li {
    display: flex;
    align-items: center;
    gap: 10px;
    font-size: 10.5px;
    color: var(--ink-grey);
    letter-spacing: 0.8px;
    line-height: 19px;
  }
  .contact-list svg { width: 11px; height: 11px; flex: none; }
  .address {
    position: absolute;
    left: 34px;
    top: 262px;
    font-size: 10.5px;
    color: var(--ink-grey);
    letter-spacing: 0.8px;
    line-height: 17px;
  }
</style>
</head>
<body>

  <section class="card card--front" aria-label="Business card front">
    <svg class="wave-wash" viewBox="0 0 240 320" role="img" aria-label="Faint water and flame wash decoration">
      <defs>
        <linearGradient id="washFront" x1="0" y1="0" x2="1" y2="0">
          <stop offset="0" stop-color="var(--wash-blue)" />
          <stop offset="0.55" stop-color="var(--wash-blue)" />
          <stop offset="1" stop-color="var(--wash-peach)" />
        </linearGradient>
      </defs>
      <path d="M40 0 C 90 60, 60 140, 90 220 C 110 270, 150 300, 170 320 L240 320 L240 0 Z" fill="url(#washFront)" />
    </svg>
    <div class="brand-name"><span class="brand-dot"></span>Vantor Plumbing &amp; Gas</div>
    <p class="front-web">www.vantorplumbingandgas.example</p>
  </section>

  <section class="card card--back" aria-label="Business card back">
    <svg class="wave-wash" viewBox="0 0 240 320" role="img" aria-label="Faint water and flame wash decoration">
      <defs>
        <linearGradient id="washBack" x1="0" y1="0" x2="1" y2="0">
          <stop offset="0" stop-color="var(--wash-blue)" />
          <stop offset="0.55" stop-color="var(--wash-blue)" />
          <stop offset="1" stop-color="var(--wash-peach)" />
        </linearGradient>
      </defs>
      <path d="M40 0 C 90 60, 60 140, 90 220 C 110 270, 150 300, 170 320 L240 320 L240 0 Z" fill="url(#washBack)" />
    </svg>

    <div class="brand-name"><span class="brand-dot"></span>Vantor Plumbing &amp; Gas</div>

    <div class="person">
      <p class="person-name">Warren Dohey</p>
      <p class="person-role">Director</p>
    </div>

    <ul class="contact-list">
      <li>
        <svg viewBox="0 0 12 12" aria-hidden="true"><path d="M2.5 1 L4.5 1 L5.2 3.6 L4 4.6 C4.7 6 6 7.3 7.4 8 L8.4 6.8 L11 7.5 L11 9.5 C11 10.3 10.3 11 9.5 11 C5 11 1 7 1 2.5 C1 1.7 1.7 1 2.5 1 Z" fill="var(--brand-blue)"/></svg>
        027 581 9043
      </li>
      <li>
        <svg viewBox="0 0 12 12" aria-hidden="true"><rect x="3" y="1" width="6" height="3" fill="var(--brand-blue)"/><rect x="1" y="4.5" width="10" height="5" rx="1" fill="var(--brand-blue)"/><rect x="3" y="8" width="6" height="3" fill="var(--brand-blue)"/></svg>
        000 000-0000
      </li>
      <li>
        <svg viewBox="0 0 12 12" aria-hidden="true"><rect x="1" y="2.5" width="10" height="7" fill="none" stroke="var(--brand-blue)" stroke-width="1.3"/><path d="M1 2.8 L6 6.5 L11 2.8" fill="none" stroke="var(--brand-blue)" stroke-width="1.3"/></svg>
        warren@vantorplumbingandgas.example
      </li>
      <li>
        <svg viewBox="0 0 12 12" aria-hidden="true"><circle cx="6" cy="6" r="5" fill="var(--brand-blue)"/><path d="M1 6 H11 M6 1 C3.5 4 3.5 8 6 11 M6 1 C8.5 4 8.5 8 6 11" fill="none" stroke="#fff" stroke-width="0.8"/></svg>
        www.vantorplumbingandgas.example
      </li>
    </ul>

    <p class="address">PO Box 7816<br>Palmerston North 4472</p>
  </section>

</body>
</html>
```